Cosmetic Dentist Practice needs stationery package/logo

I need a letterhead, envelope and business card for a cosmetic and Dental Inplant practice in an upscale part of Houston. The business card will be a size 3.5 x 2 and the letterhead will be 8.5" x 11" with a standard #10 envelope.
I have uploaded a file with an idea that the dentist had for his cards. Please note that this is not the size that the card should be. It does provide the information required.
Updates
Thank you all for your submissions. They were each unique and special in their own way. My client has made a selection that he feels best meets his needs. I appreciate each of you taking the time to offer designs. Good luck to each of you...I hope to see you back in MarblePost on future projects.
Industry/Entity Type
Business
Look and feel
Each slider illustrates characteristics of the customer's brand and the style your logo design should communicate.

```html
<!DOCTYPE html>
<html lang="en">
<head>
<meta charset="utf-8">
<title>Riverbend Smile Restorative Studio – #10 Envelope</title>
<link rel="stylesheet" href="https://fonts.googleapis.com/css2?family=Pathway+Gothic+One&family=Rokkitt:wght@700&display=swap">
<style>
  :root {
    --backdrop: #f2f2f2;
    --paper: #ffffff;
    --paper-edge: #d6d6d6;
    --ink: #1e1e1e;
  }
  html, body {
    margin: 0;
    padding: 0;
    width: 1200px;
    height: 719px;
    overflow: hidden;
    background: var(--backdrop);
  }
  .canvas {
    position: relative;
    width: 1200px;
    height: 719px;
  }
  .envelope {
    position: absolute;
    left: 45px;
    top: 121px;
    width: 1110px;
    height: 477px;
    background: var(--paper);
    border: 1px solid var(--paper-edge);
    box-sizing: border-box;
  }
  .return-address {
    position: absolute;
    left: 40px;
    top: 60px;
    color: var(--ink);
  }
  .practice-name {
    margin: 0;
    font-family: "Pathway Gothic One", sans-serif;
    font-weight: 400;
    font-size: 40px;
    line-height: 38px;
    letter-spacing: 2px;
    text-transform: uppercase;
  }
  .practice-name span {
    display: block;
  }
  .doctor-name {
    margin: 4px 0 0 14px;
    font-family: "Rokkitt", serif;
    font-weight: 700;
    font-size: 19px;
    line-height: 20px;
    text-transform: uppercase;
    letter-spacing: 0.2px;
  }
  .street-address {
    margin: 6px 0 0 36px;
    font-family: "Rokkitt", serif;
    font-weight: 700;
    font-size: 12px;
    line-height: 12px;
    font-style: normal;
  }
</style>
</head>
<body>
  <main class="canvas">
    <section class="envelope" aria-label="Number 10 envelope front">
      <div class="return-address">
        <h1 class="practice-name">
          <span>Riverbend Smile</span>
          <span>Restorative Studio</span>
        </h1>
        <p class="doctor-name">Daniel Moreno, D.D.S., PLLC</p>
        <address class="street-address">
          84 Cedar Crest Lane Suite 210,<br>
          W. Houston, TX 77031
        </address>
      </div>
    </section>
  </main>
</body>
</html>
```